Spread for a luxury home magazine

- introduce owner and team with headshots and bios
- list benefits of choosing our title company
- luxury/elegant aesthetic

Will send more headshots and bios as things progress

```html
<!DOCTYPE html>
<html lang="en">
<head>
<meta charset="utf-8">
<title>Meet the Team – Magazine Spread</title>
<link href="https://fonts.googleapis.com/css2?family=Montserrat:wght@300;400;700&display=swap" rel="stylesheet">
<style>
  :root{
    --backdrop:#c4c4c4;
    --ink:#141414;
    --paper:#ffffff;
    --accent-red:#e3202b;
    --ring-blue:#29a9e0;
    --ring-yellow:#f2e300;
    --body-dark:#5a5a5a;
    --body-light:#ececec;
  }
  *{margin:0;padding:0;box-sizing:border-box}
  html,body{width:954px;height:1200px;overflow:hidden;background:var(--backdrop)}
  body{font-family:'Montserrat',sans-serif;position:relative}
  .spread{position:absolute;left:10px;top:330px;width:934px;height:540px;display:flex;box-shadow:0 4px 10px rgba(0,0,0,.35)}
  .page{position:relative;width:467px;height:540px;overflow:hidden}
  .row{position:absolute;left:0;width:467px}
  .row-1{top:0;height:178px}
  .row-2{top:178px;height:182px}
  .row-3{top:360px;height:180px}
  .on-light{background:var(--paper);color:var(--body-dark)}
  .on-dark{background:var(--ink);color:var(--body-light)}
  .pill-band{position:absolute;left:30px;top:0;right:0;height:182px;background:var(--ink);border-radius:91px 0 0 91px}
  .bio{position:absolute;font-weight:300;font-size:7.1px;line-height:8.6px;text-align:justify;hyphens:auto}
  .bio p+p{margin-top:8.6px}
  .bio.compact{font-size:5.6px;line-height:6.9px}
  .bio.compact p+p{margin-top:6.9px}
  .name{font-weight:700;font-size:17px;line-height:18px;letter-spacing:.2px;text-transform:uppercase;margin-bottom:3px}
  .on-light .name{color:var(--ink)}
  .on-dark .name,.pill-band .name{color:var(--paper)}
  .name .first{color:var(--accent-red)}
  .pill-band .bio{color:var(--body-light)}
  .headshot{position:absolute;width:112px;height:112px}
</style>
</head>
<body>
<svg width="0" height="0" style="position:absolute" aria-hidden="true">
  <defs>
    <radialGradient id="tone-warm" cx="50%" cy="40%" r="60%">
      <stop offset="0" stop-color="#c9a184"/><stop offset="1" stop-color="#6b5a46"/>
    </radialGradient>
    <radialGradient id="tone-grey" cx="50%" cy="40%" r="60%">
      <stop offset="0" stop-color="#b59a8e"/><stop offset="1" stop-color="#7c7f86"/>
    </radialGradient>
    <radialGradient id="tone-green" cx="50%" cy="40%" r="60%">
      <stop offset="0" stop-color="#c7a493"/><stop offset="1" stop-color="#5b6650"/>
    </radialGradient>
  </defs>
</svg>

<main class="spread">
  <section class="page page-left">
    <article class="row row-1 on-light">
      <div class="bio" style="left:30px;top:27px;width:281px">
        <h2 class="name"><span class="first">Brooke</span> Lindqvist</h2>
        <p>From the sunny coast of California to the mountainous resort-style lake town of Coeur d'Alene, Idaho to now, the great state of Texas, my passion for providing exceptional service in the real estate industry has been unwavering. As an Escrow Assistant, I bring 4 years of experience in facilitating smooth transactions and ensuring client satisfaction. My escrow experience has allowed me to flourish into my current role with Keystone Title, where my knowledge of what takes place behind the scenes, always lets me be one step ahead.</p>
        <p>Outside of work, I enjoy being active, traveling and you cannot keep me away from the water. Being an aunt and a faithful Golden Gulls fan are my two favorite titles, and I can't wait to continue to see what San Antonio sports has to offer.</p>
      </div>
      <svg class="headshot" style="left:326px;top:31px" viewBox="0 0 120 120" role="img" aria-label="Headshot of Brooke Lindqvist">
        <circle cx="60" cy="60" r="50" fill="url(#tone-warm)" stroke="#222" stroke-width="1"/>
        <circle cx="58" cy="57" r="55" fill="none" stroke="var(--accent-red)" stroke-width="1.4"/>
        <circle cx="63" cy="60" r="55" fill="none" stroke="var(--ring-blue)" stroke-width="1.4"/>
        <circle cx="60" cy="63" r="55" fill="none" stroke="var(--ring-yellow)" stroke-width="1.4"/>
      </svg>
    </article>

    <article class="row row-2 on-light">
      <div class="pill-band">
        <svg class="headshot" style="left:23px;top:32px" viewBox="0 0 120 120" role="img" aria-label="Headshot of Paige Whitford">
          <circle cx="60" cy="60" r="50" fill="url(#tone-grey)" stroke="#222" stroke-width="1"/>
          <circle cx="58" cy="57" r="55" fill="none" stroke="var(--accent-red)" stroke-width="1.4"/>
          <circle cx="63" cy="60" r="55" fill="none" stroke="var(--ring-blue)" stroke-width="1.4"/>
          <circle cx="60" cy="63" r="55" fill="none" stroke="var(--ring-yellow)" stroke-width="1.4"/>
        </svg>
        <div class="bio" style="left:147px;top:16px;width:259px">
          <h2 class="name"><span class="first">Paige</span> Whitford</h2>
          <p>Recently moving from DFW, I have a hunger to grow my market in South Texas and San Antonio. Building my book of business and providing the best service in SA is my daily driver to get out of my comfort zone and generate new leads that will turn into life-long clients. Going along with that is acceptance of change. I welcome new systems and any industry changes, which I tend to use to my advantage. Working in numerous environments within real estate allows my flexible and adaptable personality to flourish.</p>
          <p>I personally enjoy living an active lifestyle. Whether it's running, hiking, or golfing, you will always find me on the go and looking for the next best version of myself. I am an avid Dallas sports fan; always supporting my Drovers, Lawmen, and Outlaws.</p>
        </div>
      </div>
    </article>

    <article class="row row-3 on-light">
      <div class="bio" style="left:30px;top:12px;width:281px">
        <h2 class="name"><span class="first">Nora</span> Castell</h2>
        <p>I've been in Real Estate for over 10 years, starting as a marketing assistant for a real estate publication which grew into transaction coordinating and office managing. Those years of experiences allowed me to learn Commercial, Residential and Farm &amp; Ranch transactions like the back of my hand. Always looking toward an opportunity to learn, I decided to venture into an Escrow and apply the transaction coordinating touch to every file while finishing every closing with a special and engaging closing experience. After all, it's not every day you buy or sell a home, and that should be celebrated!</p>
        <p>When I am not in the office creating memorable closing experiences, you can find me on a running or hiking trail with my sweet husband, Doberman, and German Shepherd. I find Zen in cooking and breadmaking, especially to Carb-load before a half marathon race weekend. Saturday nights and Sunday mornings are for Grand Prix racing or watching the Crown Saga extended edition again!</p>
      </div>
      <svg class="headshot" style="left:326px;top:30px" viewBox="0 0 120 120" role="img" aria-label="Headshot of Nora Castell">
        <circle cx="60" cy="60" r="50" fill="url(#tone-green)" stroke="#222" stroke-width="1"/>
        <circle cx="58" cy="57" r="55" fill="none" stroke="var(--accent-red)" stroke-width="1.4"/>
        <circle cx="63" cy="60" r="55" fill="none" stroke="var(--ring-blue)" stroke-width="1.4"/>
        <circle cx="60" cy="63" r="55" fill="none" stroke="var(--ring-yellow)" stroke-width="1.4"/>
      </svg>
    </article>
  </section>

  <section class="page page-right">
    <article class="row row-1 on-dark">
      <div class="bio" style="left:31px;top:27px;width:281px">
        <h2 class="name"><span class="first">Celeste</span> Harmon</h2>
        <p>The GIF queen of our office, I am a fun &amp; spunky closer who works with all kinds of agents: from luxury closings to meticulously assisting new agents, from accepted offer to the closing table. When you start off your week with me, you're going to kick off your week on a high note.</p>
        <p>My energy and caring nature will have your clients leaving our office excited and ready to begin the newest chapter in their life in their new home!</p>
      </div>
      <svg class="headshot" style="left:324px;top:31px" viewBox="0 0 120 120" role="img" aria-label="Headshot of Celeste Harmon">
        <circle cx="60" cy="60" r="50" fill="url(#tone-grey)" stroke="#ddd" stroke-width="1"/>
        <circle cx="58" cy="57" r="55" fill="none" stroke="var(--accent-red)" stroke-width="1.4"/>
        <circle cx="63" cy="60" r="55" fill="none" stroke="var(--ring-blue)" stroke-width="1.4"/>
        <circle cx="60" cy="63" r="55" fill="none" stroke="var(--ring-yellow)" stroke-width="1.4"/>
      </svg>
    </article>

    <article class="row row-2 on-light">
      <svg class="headshot" style="left:30px;top:35px" viewBox="0 0 120 120" role="img" aria-label="Headshot of Marisol Vance">
        <circle cx="60" cy="60" r="50" fill="url(#tone-grey)" stroke="#222" stroke-width="1"/>
        <circle cx="58" cy="57" r="55" fill="none" stroke="var(--accent-red)" stroke-width="1.4"/>
        <circle cx="63" cy="60" r="55" fill="none" stroke="var(--ring-blue)" stroke-width="1.4"/>
        <circle cx="60" cy="63" r="55" fill="none" stroke="var(--ring-yellow)" stroke-width="1.4"/>
      </svg>
      <div class="bio" style="left:156px;top:30px;width:280px">
        <h2 class="name"><span class="first">Marisol</span> Vance</h2>
        <p>I believe that the best thing I can do for my clients is to be kind and warm, as if you were working with a real estate guardian angel. I am always going to look out for you no matter what, just like I do for my family. Having worked as a realtor with HomeCrest Realty for 13 years and going on 9 years in title, I will leave no stone unturned when it comes to attention to detail.</p>
        <p>My experience, quality of work and attentiveness to our partners is a commodity that personifies our company's standard to serve your clients and their families. I am also BILINGUAL!</p>
      </div>
    </article>

    <article class="row row-3 on-dark">
      <div class="bio compact" style="left:31px;top:12px;width:280px">
        <h2 class="name"><span class="first">Marco</span> Reyes</h2>
        <p>I am a 9-year Navy veteran and computer science professional. I am an AHU alum (Dec '22) and possess a BS in Computer Science with a focus in Emerging Tech, and a BA in Theater Arts with a focus in Playwriting. As for my Navy experience, I've led Sailors into combat zones during two deployments in the Mediterranean and various gulf coasts surrounding Africa. I have also led joint forces through missions at the National Defense Office.</p>
        <p>I am now a blessed husband to a beautiful wife and father of two beautiful girls. My "why" for being in Title is that having purchased two beautiful homes of my own, with an awesome realtor and awesome lender on both deals, I had a terrible closing experience on both deals that no one should have to experience during an already stressful process. As a buyer who didn't know any better, both of those realtors and lenders lost my business as a repeat client, and I darn sure didn't refer them to anyone. So now, it is MY MISSION to ensure that EVERY-ONE gets an amazing closing experience, regardless of price point. For fun, I love my Lakeshore Hounds &amp; River City Riders. I also enjoy pretty much anything competitive and have played every sport ever created, hoops being my specialty. Lastly, if you ever need a resource for fantasy football advice, I'm fresh off 4 trophies out of 5 leagues in 2023!</p>
      </div>
      <svg class="headshot" style="left:324px;top:30px" viewBox="0 0 120 120" role="img" aria-label="Headshot of Marco Reyes">
        <circle cx="60" cy="60" r="50" fill="url(#tone-green)" stroke="#ddd" stroke-width="1"/>
        <circle cx="58" cy="57" r="55" fill="none" stroke="var(--accent-red)" stroke-width="1.4"/>
        <circle cx="63" cy="60" r="55" fill="none" stroke="var(--ring-blue)" stroke-width="1.4"/>
        <circle cx="60" cy="63" r="55" fill="none" stroke="var(--ring-yellow)" stroke-width="1.4"/>
      </svg>
    </article>
  </section>
</main>
</body>
</html>
```